Beauty Clinic Treatment Menu (Lumen Nails & Beauty)

Needing a treatment menu designed for a beauty clinic in Harbourton, New Zealand. Like the colours grey, pink, white.
Elegant, Modern and feminine

Lumen Nails & Beauty
Karen Pell
Suite 7, 48 Tainui Street
Harbourton
0273816240
Karen.lumen@mailbox.test
lumenbeauty.co.nz

Target Market(s)

Females

Industry/Entity Type

Beauty Salon

Font styles to use
Serif

Colors

Requirements
Must have
• Chatterly and Snapgrid logo

```html
<!DOCTYPE html>
<html lang="en">
<head>
<meta charset="utf-8">
<title>Lumen Nails &amp; Beauty – Treatment Menu</title>
<link href="https://fonts.googleapis.com/css2?family=Cinzel:wght@400;600&family=Cormorant+Garamond:wght@400;500&display=swap" rel="stylesheet">
<style>
  :root {
    --pink: #e3c3c6;
    --grey: #d9d9d9;
    --white: #ffffff;
    --ink: #4f4a4c;
    --ink-soft: #8a8284;
    --rose-gold: #c29a86;
  }
  * { margin: 0; padding: 0; box-sizing: border-box; }
  html, body { width: 769px; height: 1200px; overflow: hidden; background: var(--white); }
  body { position: relative; font-family: "Cinzel", serif; color: var(--ink); }

  /* Outside spread */
  .outside { position: absolute; left: 0; top: 0; width: 769px; height: 600px; background: var(--white); }
  .contact-panel { position: absolute; left: 0; top: 158px; width: 256px; height: 250px;
    border-top: 1px dashed var(--ink-soft); border-bottom: 1px dashed var(--ink-soft); }
  .contact { position: absolute; left: 30px; top: 42px; font-size: 7.5px; letter-spacing: 1.4px; line-height: 19px; color: var(--ink-soft); list-style: none; }
  .cover { position: absolute; left: 256px; top: 20px; width: 513px; height: 542px; background: var(--pink); }
  .cover-logo { position: absolute; left: 234px; top: 48px; width: 154px; height: 154px; border-radius: 50%; background: var(--white);
    display: flex; align-items: center; justify-content: center; }
  .brand-word { font-family: "Cormorant Garamond", serif; font-size: 32px; font-weight: 400; color: var(--rose-gold); letter-spacing: 1px; }
  .services { color: var(--white); font-size: 8px; letter-spacing: 2.4px; line-height: 16px; text-align: center; }
  .cover-services { position: absolute; left: 211px; top: 226px; width: 200px; }
  .back-services { position: absolute; left: 16px; top: 428px; width: 110px; font-size: 5.5px; line-height: 11px; letter-spacing: 1.2px; text-align: left; }
  .card { position: absolute; left: 325px; top: 472px; width: 175px; height: 78px; background: var(--white);
    box-shadow: 0 1px 4px rgba(0,0,0,.15); display: flex; align-items: center; justify-content: center; }
  .card-ring { width: 60px; height: 60px; border: 1px solid var(--rose-gold); border-radius: 50%; display: flex; align-items: center; justify-content: center; }
  .card .brand-word { font-size: 15px; }

  /* Inside menu */
  .menu { position: absolute; left: 0; top: 605px; width: 769px; height: 595px; background: var(--grey); }
  .menu-col-pink { position: absolute; left: 256px; top: 0; width: 256px; height: 595px; background: var(--pink); }
  .menu-title { position: absolute; left: 0; width: 769px; top: 30px; text-align: center; font-size: 24px; letter-spacing: 10px; font-weight: 400; color: var(--ink); }
  .col { position: absolute; top: 95px; text-align: center; }
  .col-nails { left: 20px; width: 216px; }
  .col-facials { left: 270px; width: 228px; }
  .col-body { left: 524px; width: 230px; }
  .section-title { font-size: 10px; font-weight: 600; letter-spacing: 1.6px; height: 14px; }
  .item-title { font-size: 6.5px; font-weight: 600; letter-spacing: 1px; margin-bottom: 6px; }
  .price { font-size: 6.5px; letter-spacing: 1px; line-height: 15px; color: var(--ink); }
  .note { font-family: "Cormorant Garamond", serif; font-size: 7px; line-height: 10px; color: var(--ink-soft); }

  .col-nails .section-title { margin-bottom: 46px; }
  .nail-group { margin-bottom: 34px; }
  .nail-group.tight { margin-bottom: 10px; }
  .col-facials .section-title { margin-bottom: 38px; }
  .treatment { margin-bottom: 20px; }
  .treatment .item-title { margin-bottom: 5px; }
  .col-body .section-title { margin-bottom: 13px; }
  .body-group { margin-bottom: 32px; }
</style>
</head>
<body>
  <section class="outside">
    <div class="contact-panel">
      <ul class="contact">
        <li>LUMEN NAILS &amp; BEAUTY</li>
        <li>KAREN PELL</li>
        <li>SUITE 7, 48 TAINUI STREET</li>
        <li>HARBOURTON</li>
        <li>0273816240</li>
        <li>KAREN.LUMEN@MAILBOX.TEST</li>
        <li>LUMENBEAUTY.CO.NZ</li>
      </ul>
    </div>
    <div class="cover">
      <div class="cover-logo"><span class="brand-word">Lumen</span></div>
      <div class="services cover-services">NAILS | FACIALS<br>EYES | FACE | BODY</div>
      <div class="services back-services">NAILS | FACIALS<br>EYES | FACE | BODY</div>
    </div>
    <div class="card"><div class="card-ring"><span class="brand-word">Lumen</span></div></div>
  </section>

  <section class="menu">
    <div class="menu-col-pink"></div>
    <h1 class="menu-title">MENU</h1>

    <div class="col col-nails">
      <h2 class="section-title">NAILS</h2>
      <div class="nail-group">
        <h3 class="item-title">MANICURE</h3>
        <p class="price">GEL POLISH | $45</p>
        <p class="price">REGULAR POLISH | $35</p>
      </div>
      <div class="nail-group">
        <h3 class="item-title">PEDICURE</h3>
        <p class="price">GEL POLISH | $50</p>
        <p class="price">REGULAR POLISH | $40</p>
      </div>
      <div class="nail-group">
        <h3 class="item-title">LUXURY PEDICURE</h3>
        <p class="note">Includes soak, exfoliation,<br>foot scrub and massage</p>
        <p class="price">GEL POLISH | $65</p>
        <p class="price">REGULAR POLISH | $55</p>
      </div>
      <div class="nail-group tight">
        <h3 class="item-title">REMOVAL &amp; NAIL TIDY | $20</h3>
      </div>
      <div class="nail-group">
        <h3 class="item-title">ADD ON</h3>
        <p class="price">GEL REMOVAL | $10</p>
        <p class="price">ART | $5 &nbsp; 3D | $10</p>
        <p class="price">BUILDER GEL | $15</p>
        <p class="price">NAIL REPAIR | $5</p>
      </div>
    </div>

    <div class="col col-facials">
      <h2 class="section-title">FACIALS</h2>
      <div class="treatment">
        <h3 class="item-title">DEEP CLEANSING FACIAL | $75</h3>
        <p class="note">60 minutes</p>
        <p class="note">Removes build up of dead skin cells, leaves the<br>skin feeling soft and refreshed</p>
      </div>
      <div class="treatment">
        <h3 class="item-title">THERAPEUTIC FACIAL | $80</h3>
        <p class="note">60 minutes</p>
        <p class="note">Tailored to suit your skin and its needs</p>
      </div>
      <div class="treatment">
        <h3 class="item-title">REJUVENATION FACIAL | $90</h3>
        <p class="note">60 minutes</p>
        <p class="note">An instant glow to brighten tired skin<br>and restore hydration</p>
      </div>
      <div class="treatment">
        <h3 class="item-title">BIO ENZYME FACIAL | $95</h3>
        <p class="note">60 minutes</p>
        <p class="note">Hydrating, deep exfoliation for smoother<br>skin texture and appearance</p>
      </div>
      <div class="treatment">
        <h3 class="item-title">DERMAPLANING | $80</h3>
        <p class="note">45 minutes</p>
        <p class="note">Creates a smooth skin surface that<br>also removes soft facial hairs</p>
      </div>
    </div>

    <div class="col col-body">
      <div class="body-group">
        <h2 class="section-title">EYES</h2>
        <p class="price">BROW LASH LIFT | $65</p>
        <p class="price">EYEBROW SHAPE | $20</p>
        <p class="price">EYEBROW TINT | $15</p>
        <p class="price">EYELASH TINT | $20</p>
        <p class="price">BROW COMBO | $30</p>
      </div>
      <div class="body-group">
        <h2 class="section-title">FACE</h2>
        <p class="price">LIP | $10</p>
        <p class="price">CHIN | $10</p>
      </div>
      <div class="body-group">
        <h2 class="section-title">BODY</h2>
        <p class="price">UNDERARM | $20</p>
        <p class="price">1/2 LEG | $30</p>
        <p class="price">3/4 LEG | $35</p>
        <p class="price">1/2 ARM | $20</p>
        <p class="price">FULL ARM | $30</p>
        <p class="price">BIKINI | $20</p>
        <p class="price">EXTENDED BIKINI | $30</p>
        <p class="price">BRAZILIAN 1ST TIME | $60</p>
        <p class="price">BRAZILIAN (4-6 WEEKS) | $50</p>
        <p class="price">BACK | $45</p>
      </div>
    </div>
  </section>
</body>
</html>
```